Need a logo and business card design for my electrical company.
Company name is Kestrel Grid Electrical
In the bottow right hand corner i need
E.C. 784213 for the momument till i get my contractors license number sent to me.
Design i want black back ground with a picture of Thor's hammer and lighting hitting the top of it.

Electrical

Owner Darren Holcott Phone number 0471382905 email kestrelgridelectrical@nerimail.com facebook page Kestrel Grid Electrical

```html
<!DOCTYPE html>
<html lang="en">
<head>
<meta charset="utf-8">
<title>Kestrel Grid Electrical – Business Card</title>
<link rel="stylesheet" href="https://fonts.googleapis.com/css2?family=Open+Sans:wght@400;700&display=swap">
<style>
  :root {
    --backdrop: #e4e4e1;
    --card: #1c1c1c;
    --card-edge: #151515;
    --yellow: #f2d82a;
    --white: #f4f4f4;
    --grey: #bdbdbd;
    --ink: #1c1c1c;
  }
  * { box-sizing: border-box; margin: 0; padding: 0; }
  html, body { width: 1200px; height: 799px; overflow: hidden; }
  body {
    background: var(--backdrop);
    font-family: "Open Sans", Arial, sans-serif;
    position: relative;
  }
  .card {
    position: absolute;
    top: 130px;
    width: 540px;
    height: 309px;
    background: var(--card);
    border: 6px solid var(--card-edge);
    overflow: hidden;
  }
  .card--contact { left: 40px; }
  .card--brand { left: 620px; }

  /* contact side */
  .contact {
    position: absolute;
    left: 250px;
    top: 36px;
    color: var(--white);
  }
  .contact__name { font-size: 20px; font-weight: 400; letter-spacing: 0.5px; }
  .contact__title { font-size: 11px; color: var(--yellow); margin-bottom: 12px; }
  .contact__line {
    display: flex; align-items: center; gap: 8px;
    font-size: 11px; color: var(--grey); margin-bottom: 6px;
  }
  .contact__line svg { width: 12px; height: 12px; flex: none; }
  .social-bar {
    position: absolute;
    left: 230px; top: 146px;
    width: 268px; height: 16px;
    background: var(--yellow);
    display: flex; align-items: center; justify-content: flex-end;
    padding-right: 10px; gap: 5px;
  }
  .social-bar__dot { width: 9px; height: 9px; background: var(--ink); }
  .social-bar__handle { font-size: 10px; color: var(--ink); margin-left: 3px; }
  .social-bar__end {
    position: absolute;
    left: 498px; top: 146px;
    width: 32px; height: 16px;
    background: var(--white);
  }
  .licence-bar {
    position: absolute;
    left: 0; bottom: 14px;
    width: 100%; height: 20px;
    background: var(--yellow);
    display: flex; align-items: center;
    padding-left: 28px;
    font-size: 12px; color: var(--ink); letter-spacing: 1px;
  }

  /* brand mark */
  .brand {
    position: absolute;
    display: flex; align-items: center; gap: 10px;
  }
  .brand__square { background: var(--yellow); flex: none; }
  .brand__name {
    font-weight: 700; color: var(--white);
    text-transform: uppercase; line-height: 1.05;
  }
  .card--contact .brand { left: 30px; top: 186px; }
  .card--contact .brand__square { width: 16px; height: 16px; }
  .card--contact .brand__name { font-size: 17px; }

  .card--brand .brand { right: 28px; top: 34px; }
  .card--brand .brand__square { width: 20px; height: 20px; }
  .card--brand .brand__name { font-size: 22px; }

  .brand-feature {
    position: absolute;
    left: 62px; top: 118px;
    width: 130px; height: 130px;
    background: var(--yellow);
  }

  /* standalone mark */
  .brand--standalone { right: 60px; bottom: 80px; }
  .brand--standalone .brand__square { width: 40px; height: 40px; }
  .brand--standalone .brand__name { font-size: 40px; color: var(--ink); }
</style>
</head>
<body>

  <section class="card card--contact">
    <div class="contact">
      <p class="contact__name">Darren Holcott</p>
      <p class="contact__title">Owner</p>
      <p class="contact__line">
        <svg viewBox="0 0 12 12"><path fill="#f2d82a" d="M2 1h3l1 3-2 1a7 7 0 0 0 3 3l1-2 3 1v3c0 1-1 1-1 1A10 10 0 0 1 1 2s0-1 1-1z"/></svg>
        0471382905
      </p>
      <p class="contact__line">
        <svg viewBox="0 0 12 12"><rect x="1" y="2.5" width="10" height="7" fill="#f2d82a"/><path d="M1 2.5l5 4 5-4" fill="none" stroke="#1c1c1c" stroke-width="1"/></svg>
        kestrelgridelectrical@nerimail.com
      </p>
    </div>

    <div class="social-bar">
      <span class="social-bar__dot"></span>
      <span class="social-bar__dot"></span>
      <span class="social-bar__dot"></span>
      <span class="social-bar__handle">/kestrelgrid</span>
    </div>
    <div class="social-bar__end"></div>

    <div class="brand">
      <span class="brand__square"></span>
      <p class="brand__name">Kestrel Grid<br>Electrical</p>
    </div>

    <div class="licence-bar">E.C. 784213</div>
  </section>

  <section class="card card--brand">
    <div class="brand">
      <span class="brand__square"></span>
      <p class="brand__name">Kestrel Grid<br>Electrical</p>
    </div>
    <div class="brand-feature" role="img" aria-label="Large brand symbol area in yellow"></div>
  </section>

  <div class="brand brand--standalone">
    <span class="brand__square"></span>
    <p class="brand__name">Kestrel Grid<br>Electrical</p>
  </div>

</body>
</html>
```